Business Cards for IT Consulting Company (Managed Service Provider)

I am looking to have some business cards printed and would like some designs. We are an IT Consulting company based in Vancouver BC. I would like a nice clean and modern look to the cards. I have uploaded all the versions of my logo so parts can be used as needed. Here is a snippit from our website homepage:

Kelbrook Systems Ltd. is an IT Solutions Partner located in Vancouver BC, Canada. We offer IT solutions and support to customers in the greater Vancouver Area. With expertise in Microsoft platforms, as well as Linux and Mac OSX and over 12 years experience in the IT industry, Kelbrook Systems is dedicated to offering our clients top quality service and products. We take pride in the solutions we offer our customers. The greatest compliment a client can give us is to recommend our services.

Kelbrook Systems Ltd. offers a wide range of IT services from onsite service to remote support and managed service solutions. This allows clients to choose the support path that best suits their company’s needs. Supporting many different sized companies from small to enterprise level over the past 12 years Kelbrook Systems has the experience and expertise needed to ensure things run smoothly. Allowing our clients to focus on doing business.

Revolutionizing the way IT services are delivered.

Kelbrook Systems is dedicated to providing our clients with IT solutions that work and grow with them for years to come. This philosophy helps save money in the long run instead of replacing equipment constantly. Far too often IT solutions are not well thought out and while possibly solving the problem at hand, require replacement due to growth or quality within a very short time frame. Kelbrook Systems takes pride in providing solutions that will last and be able to accommodate growth without the need for replacement.

Industry/Entity Type

Information Technology

Contact Information for Business Card

Kelbrook Systems Ltd.
(Employee Name)
Eml: (Employees Email Address)
Web: kelbrook.me
Ph: 604-555-0142

Font styles to use
Serif
Sans Serif

Requirements
Must have
• The Company logo and company colors.
Nice to have
• - Our tag line: "Revolutionizing IT Services" or "Revolutionizing the way IT services are delivered."
• - Also I really like the idea of nature and technology together blending which is sort of where my logo came from so integrating that somehow onto the business cards would be great.

```html
<!DOCTYPE html>
<html lang="en">
<head>
<meta charset="utf-8">
<title>Kelbrook Systems Ltd. — Business Cards</title>
<link href="https://fonts.googleapis.com/css2?family=Montserrat:wght@500;600;700&display=swap" rel="stylesheet">
<style>
  :root {
    --brand-blue: #0a9fd6;
    --brand-blue-pale: #7fcdec;
    --ink: #3d3d3d;
    --paper: #ffffff;
    --backdrop: #e4e5e6;
    --card-edge: rgba(0, 0, 0, 0.12);
  }
  * { margin: 0; padding: 0; box-sizing: border-box; }
  html, body {
    width: 1200px;
    height: 723px;
    overflow: hidden;
    background: var(--backdrop);
    font-family: "Montserrat", sans-serif;
  }
  .canvas {
    position: relative;
    width: 1200px;
    height: 723px;
  }
  .card {
    position: absolute;
    width: 600px;
    height: 343px;
    overflow: hidden;
    box-shadow: 0 2px 0 var(--card-edge), 0 10px 24px rgba(0, 0, 0, 0.12);
  }
  .card--back {
    left: 460px;
    top: 70px;
    background: var(--brand-blue);
  }
  .card--front {
    left: 150px;
    top: 300px;
    background: var(--paper);
  }
  .pattern-area {
    position: absolute;
    top: 0;
    left: 0;
    height: 100%;
  }
  .card--back .pattern-area {
    width: 260px;
    background: linear-gradient(90deg, var(--brand-blue-pale) 0%, var(--brand-blue) 100%);
  }
  .card--front .pattern-area {
    width: 270px;
    background: linear-gradient(90deg, var(--brand-blue) 0%, #bfe6f6 75%, var(--paper) 100%);
  }
  .brand {
    position: absolute;
    left: 300px;
    top: 78px;
    display: flex;
    align-items: center;
    gap: 10px;
  }
  .brand__dot {
    width: 26px;
    height: 26px;
    border: 2px solid var(--brand-blue);
    border-radius: 50%;
  }
  .brand__name {
    font-size: 21px;
    font-weight: 700;
    color: var(--brand-blue);
    letter-spacing: 0.2px;
  }
  .person {
    position: absolute;
    left: 300px;
    top: 140px;
  }
  .person__name {
    font-size: 19px;
    font-weight: 700;
    color: var(--ink);
    letter-spacing: 0.5px;
  }
  .person__role {
    font-size: 15px;
    font-weight: 600;
    color: var(--brand-blue);
    margin-top: 1px;
  }
  .contacts {
    position: absolute;
    left: 300px;
    top: 212px;
    list-style: none;
  }
  .contacts__item {
    display: flex;
    align-items: center;
    gap: 10px;
    height: 28px;
    font-size: 15px;
    font-weight: 500;
    color: var(--ink);
  }
  .contacts__icon {
    width: 20px;
    height: 18px;
    flex: none;
  }
</style>
</head>
<body>
<main class="canvas">

  <section class="card card--back" aria-label="Card back">
    <div class="pattern-area" role="img" aria-label="Large white outlined cube pattern on blue"></div>
  </section>

  <section class="card card--front" aria-label="Card front">
    <div class="pattern-area" role="img" aria-label="Large blue outlined cube pattern on white"></div>

    <div class="brand">
      <span class="brand__dot" aria-hidden="true"></span>
      <span class="brand__name">Kelbrook Systems Ltd.</span>
    </div>

    <div class="person">
      <p class="person__name">DANA WHITLOW</p>
      <p class="person__role">Director</p>
    </div>

    <ul class="contacts">
      <li class="contacts__item">
        <svg class="contacts__icon" viewBox="0 0 20 18" aria-hidden="true">
          <rect x="1" y="3" width="18" height="12" fill="var(--brand-blue)"/>
          <path d="M1 3 L10 10 L19 3" fill="none" stroke="#fff" stroke-width="1.6"/>
        </svg>
        YourmailAddress@kelbrook.me
      </li>
      <li class="contacts__item">
        <svg class="contacts__icon" viewBox="0 0 20 18" aria-hidden="true">
          <path d="M2 6 Q10 1 18 6 L16 8 L13 6.5 L13 5 Q10 4 7 5 L7 6.5 L4 8 Z" fill="var(--brand-blue)"/>
          <rect x="4" y="9" width="12" height="7" rx="1" fill="var(--brand-blue)"/>
          <circle cx="10" cy="12.5" r="2" fill="#fff"/>
        </svg>
        604-555-0142
      </li>
      <li class="contacts__item">
        <svg class="contacts__icon" viewBox="0 0 20 18" aria-hidden="true">
          <circle cx="10" cy="9" r="8" fill="var(--brand-blue)"/>
          <ellipse cx="10" cy="9" rx="3.5" ry="8" fill="none" stroke="#fff" stroke-width="1"/>
          <line x1="2" y1="9" x2="18" y2="9" stroke="#fff" stroke-width="1"/>
        </svg>
        kelbrook.me
      </li>
    </ul>
  </section>

</main>
</body>
</html>
```